Luxurious Rustic Cottage Accommodation brochure design

I would like a trifold brochure design to continue the theme I already have established on my website www.atbellcroft.com.au The basic theme uses the logo from the website, it is called "At Bellcroft" B & B Private Cottages and has black background with use of gold for borders and highlights. The accommodation is in the hinterland region of the Sunshine Coast, Queensland, Australia. I have 4 separate private cottages which I would like to include information & pictures about each as per details on the website mentioned. Features to highlight include ocean views, log fires, spa baths, romance, nature. Accommodation is suitable for couples, family, small group or wedding party, special occasion getways. Package inclusions to be highlighted are breakfast hamper, complimentary chocolates & champagne, pamper products, optional inclusions are cheese platter, relaxation massage. I would like location to be included by way of a map, contact details (website, email & mobile phone) to also be included.
There are pictures on the website which I can provide high resolution for brochure printing as required. Some more images have been uploaded for optional use.
Accommodation

```html
<!DOCTYPE html>
<html lang="en">
<head>
<meta charset="utf-8">
<title>At Bellcroft – Trifold Brochure</title>
<link href="https://fonts.googleapis.com/css2?family=Open+Sans:wght@400;600;700&family=Pinyon+Script&display=swap" rel="stylesheet">
<style>
  :root{
    --black:#000;
    --gold:#c0963f;
    --gold-light:#d9b15b;
    --ink:#1f1608;
    --white:#fff;
    --muted:#8a8070;
    --page:#3a3a3a;
    --sans:'Open Sans', Arial, sans-serif;
    --script:'Pinyon Script', cursive;
  }
  *{box-sizing:border-box;margin:0;padding:0}
  html,body{width:1186px;height:1200px;overflow:hidden;background:var(--page);font-family:var(--sans)}
  h1,h2,p{font-weight:400}
  .brochure{position:absolute;left:78px;top:200px;width:1030px;height:800px;background:var(--black)}
  .panel{position:absolute;top:13px;height:774px;overflow:hidden}

  /* Cabins panel */
  .cabins{left:13px;width:322px;background:var(--white)}
  .cabins-header{position:absolute;left:0;top:0;width:322px;height:110px}
  .cabins-title{position:absolute;left:17px;top:18px;font-family:var(--script);font-size:40px;line-height:48px;color:var(--ink)}
  .cabin-name{position:absolute;left:7px;font-size:17px;line-height:22px;font-weight:400;color:#111}
  .cabin-photo{position:absolute;left:7px;width:104px;height:104px}
  .cabin-text{position:absolute;left:118px;width:190px;font-size:11.1px;line-height:15.5px;letter-spacing:-0.1px;color:#111;text-align:justify;hyphens:auto}

  /* Host panel */
  .host{left:335px;width:357px;background:var(--black)}
  .host-gold{position:absolute;left:0;top:0;width:357px;height:580px;background:var(--gold)}
  .host-waves{position:absolute;left:0;top:578px;width:357px;height:60px}
  .host-frame{position:absolute;left:68px;top:20px;width:220px;height:165px;background:#111;border-radius:6px}
  .host-photo{position:absolute;left:86px;top:35px;width:185px;height:136px;background:linear-gradient(120deg,#7a8a60,#b8b0a0 45%,#c0302a 70%,#6a5a48)}
  .host-heading{position:absolute;left:0;width:357px;top:198px;text-align:center;font-family:var(--script);font-size:40px;line-height:48px;color:var(--white)}
  .host-copy{position:absolute;left:28px;width:301px;text-align:center;font-size:13.6px;line-height:18.6px;color:var(--ink)}
  .host-features{position:absolute;left:0;width:357px;top:446px;text-align:center;font-size:15.5px;line-height:22px;color:var(--white)}
  .host-book{position:absolute;left:0;width:357px;top:518px;text-align:center;color:var(--white)}
  .host-book strong{display:block;font-size:24px;font-weight:700;line-height:32px}
  .host-book span{display:block;font-size:25px;line-height:34px}
  .contact{position:absolute;left:0;width:357px;top:646px;text-align:center;color:var(--white)}
  .contact-name{font-size:15px;line-height:20px;margin-bottom:18px}
  .contact-lines{font-size:11.4px;line-height:15.6px}

  /* Cover panel */
  .cover{left:692px;width:326px;background:#000}
  .cover-top{position:absolute;left:0;top:0;width:326px;height:160px}
  .cover-scene{position:absolute;left:0;top:370px;width:326px;height:280px;background:radial-gradient(ellipse 70% 45% at 33% 30%,#fff2c8 0,#f27a78 7%,#9a3550 22%,#3a2030 48%,#120e14 72%,#000 100%)}
  .brand{position:absolute;left:0;width:326px;top:48px;text-align:center;color:var(--white)}
  .brand-mark{display:inline-block;width:14px;height:14px;border-radius:50%;background:var(--gold);vertical-align:middle;margin-right:8px}
  .brand-name{font-size:30px;vertical-align:middle;letter-spacing:1px}
  .brand-sub{font-size:8.5px;margin-top:4px;letter-spacing:.5px}
  .cover-lead{position:absolute;left:0;width:326px;top:236px;text-align:center;font-family:var(--script);font-size:23px;line-height:32px;color:var(--gold-light)}
  .cover-country{position:absolute;left:0;width:326px;top:340px;text-align:center;font-family:var(--script);font-size:36px;line-height:44px;color:var(--gold-light)}
  .cover-book{position:absolute;left:0;width:326px;top:662px;text-align:center;color:var(--white);font-size:25px;line-height:34px}
  .cover-url{position:absolute;left:0;width:326px;top:736px;text-align:center;font-family:var(--script);font-size:19px;line-height:24px;color:var(--muted)}
</style>
</head>
<body>
<div class="brochure">

  <section class="panel cabins">
    <svg class="cabins-header" viewBox="0 0 322 110" aria-hidden="true">
      <path d="M0 0H322V62C250 42 180 58 120 76C70 90 30 86 0 74Z" fill="var(--gold)"/>
      <path d="M0 78C40 92 80 88 130 74C190 58 260 50 322 66V74C260 60 190 68 130 84C80 98 40 100 0 90Z" fill="var(--gold)"/>
    </svg>
    <h1 class="cabins-title">Cabins</h1>

    <h2 class="cabin-name" style="top:110px">Drovers Song</h2>
    <div class="cabin-photo" style="top:142px;background:linear-gradient(#d8d2c8,#f2efe8 60%,#c9b9a0)" role="img" aria-label="Cabin bedroom with king size bed and breakfast tray"></div>
    <p class="cabin-text" style="top:139px">Rustic luxurious king size bed, indoor/outdoor spa bath set amongst the treetops with magical views overlooking the hinterland and beyond. Awake to the sound of birds and magnificent sunrises, fresh air on your private balcony or throw a log on the fire to create an intimate atmosphere.</p>

    <h2 class="cabin-name" style="top:285px">Koorala</h2>
    <div class="cabin-photo" style="top:317px;background:linear-gradient(#cfd8e0,#8a7a66 50%,#5c6a48)" role="img" aria-label="Timber cabin exterior among garden plants"></div>
    <p class="cabin-text" style="top:314px">Surrounded by fragrant timber, featuring hand crafted camphor furniture. Set amongst tall trees and nature with a panoramic hinterland &amp; ocean view. Misty mornings &amp; crystal clear afternoons are scenes to enjoy from the spa bath, balcony or comfy couches by the log fire. All you need for romance or to relax, revive &amp; reminisce.</p>

    <h2 class="cabin-name" style="top:475px">Selinah</h2>
    <div class="cabin-photo" style="top:510px;background:linear-gradient(135deg,#6a8a4a,#b8773a 45%,#8a5228)" role="img" aria-label="Carved timber cabin name sign in a garden"></div>
    <p class="cabin-text" style="top:507px">A luxurious escape for a couple or small family, featuring a king size bed with an option to add two single beds, a private &amp; self contained setting, hinterland &amp; coastal views, spa bath &amp; log fire. Enjoy the birds singing &amp; stunning sunrises.</p>

    <h2 class="cabin-name" style="top:625px">Lodge</h2>
    <div class="cabin-photo" style="top:659px;background:linear-gradient(#6a9ad0,#a8c2da 40%,#4a6a50 70%,#2a3a2a)" role="img" aria-label="View from the lodge over the hinterland to the ocean"></div>
    <p class="cabin-text" style="top:656px">Our Lodge accommodation features 4 bedrooms and a great open plan living space with ocean &amp; hinterland views from every aspect. An ideal gathering spot or retreat for family &amp; friends.</p>
  </section>

  <section class="panel host">
    <div class="host-gold"></div>
    <svg class="host-waves" viewBox="0 0 357 60" aria-hidden="true">
      <path d="M0 0H357V18C300 4 200 8 120 22C70 31 30 36 0 40Z" fill="var(--gold)"/>
      <path d="M0 50C40 42 100 34 160 30C230 26 300 30 357 42V48C300 36 230 34 160 38C100 42 40 50 0 58Z" fill="var(--gold)"/>
    </svg>
    <div class="host-frame"></div>
    <div class="host-photo" role="img" aria-label="Host family with their dog beside a red vintage car"></div>
    <h2 class="host-heading">Your Host</h2>
    <p class="host-copy" style="top:251px">Mark &amp; Leanne Harlow, we are classic “treechangers” and together with our 3 daughters we moved to Queensland from Northern NSW in 2005 to enjoy the beautiful hinterland lifestyle and establish our B &amp; B.</p>
    <p class="host-copy" style="top:362px">We love to have a chat, share our local knowledge and ensure you have everything to make your stay enjoyable, otherwise we pretty much leave you to enjoy your own company.</p>
    <p class="host-features">Pet Friendly / Non-Smoking<br>Complimentary Shuttle Wireless Internet<br>BBQ/Picnic Hampers</p>
    <div class="host-book"><strong>Book Now</strong><span>0400 555 218</span></div>
    <div class="contact">
      <p class="contact-name">Mark &amp; Leanne Harlow</p>
      <p class="contact-lines">Ph:&nbsp; 0400 555218<br>Email: leanne@atbellcroft.com.au<br>Bellcroft’s Rise<br>48 Ridgeview Road<br>Maple Hill&nbsp; QLD&nbsp; 4999</p>
    </div>
  </section>

  <section class="panel cover">
    <div class="cover-scene" role="img" aria-label="Sunrise over misty hinterland with a silhouetted couple and palm"></div>
    <svg class="cover-top" viewBox="0 0 326 160" aria-hidden="true">
      <path d="M0 0H326V114C250 100 190 118 130 136C80 150 40 150 0 144Z" fill="#111114"/>
      <path d="M0 144C40 150 80 150 130 136C190 118 250 100 326 114V118C250 106 190 124 130 142C80 156 40 156 0 150Z" fill="var(--gold)"/>
    </svg>
    <div class="brand">
      <span class="brand-mark"></span><span class="brand-name">At Bellcroft</span>
      <p class="brand-sub">bed &amp; breakfast &nbsp;&nbsp; private cottages</p>
    </div>
    <p class="cover-lead">The accommodation is in the<br>hinterland region of the<br>Sunshine Coast, Queensland,</p>
    <p class="cover-country">Australia</p>
    <p class="cover-book">Book Now<br>0400 555 218</p>
    <p class="cover-url">www.atbellcroft.com.au</p>
  </section>

</div>
</body>
</html>
```